Business card for a boutique travel agency VELIRANDE

we need a business card design - double sided. We would like to have a very elegant, sophisticated but modern design. we are travel consultants and our business focus is Europe, mainly the city of Paris. We would like to receive designs in white and silver, black color but if you are confident that we should pick up a color to make it different and more beautful...go ahead! We are going to give business cards to our clients and business partners. It is important to be perceived as elegant, modern and trustful. Please check jpg references.

Target Market(s)

Velirande primary clients are individuals, couples and affinity groups of high-net-worth who travel for leisure at least once per year. Seeking the ultimate travel experience, the target clients demand the finest quality activities and accommodations accompanied by a superior level of service.

Industry/Entity Type

Travel Industry

Contact Information for Business Card

Liliana Quesada
- liliana@velirande-mail.example
- +55 11 98437.5216
- velirande-mail.example
- unique travel experiences (we would like to see this signature printed as a detail)

Font styles to use
Sans Serif

Colors

Designer to choose colors to be used in the design.

Requirements
Must have
• the Velirande logo that I have attached
Nice to have
• we would like to have some nice detail, something different that shows that we care about,... we are detail oriented.
Should not have
• decorative fonts

```html
<!DOCTYPE html>
<html lang="en">
<head>
<meta charset="utf-8">
<title>Velirande – Business Card</title>
<link href="https://fonts.googleapis.com/css2?family=Great+Vibes&family=Josefin+Sans:wght@300&family=Open+Sans:wght@400&display=swap" rel="stylesheet">
<style>
  :root {
    --page-bg: #4a423d;
    --card-white: #ffffff;
    --card-black: #050505;
    --ink-dark: #111111;
    --ink-light: #f4f4f4;
    --ink-muted: #bdbdbd;
    --ring-grey: #2b2b2b;
    --rule: #6a6a6a;
  }
  * { margin: 0; padding: 0; box-sizing: border-box; }
  html, body {
    width: 1200px; height: 1200px; overflow: hidden;
    background: var(--page-bg);
  }
  .sheet {
    width: 1200px; height: 1200px;
    display: flex; flex-direction: column;
    align-items: center; justify-content: center; gap: 60px;
  }
  .card {
    position: relative;
    width: 840px; height: 480px;
    overflow: hidden;
    box-shadow: 0 8px 24px rgba(0,0,0,0.35);
  }
  /* Front */
  .card--front { background: var(--card-white); }
  .front-name {
    position: absolute; left: 150px; top: 130px;
    font-family: "Great Vibes", cursive;
    font-size: 92px; line-height: 1.05;
    color: var(--ink-dark);
  }
  .front-name span { display: block; }
  .front-name span + span { padding-left: 150px; }

  /* Back */
  .card--back { background: var(--card-black); }
  .back-ring { position: absolute; left: 0; top: 0; }
  .wordmark {
    position: absolute; left: 48px; top: 150px;
    font-family: "Josefin Sans", sans-serif; font-weight: 300;
    font-size: 60px; letter-spacing: 0.32em;
    color: var(--ink-light);
  }
  .top-rule {
    position: absolute; left: 470px; right: 0; top: 228px;
    height: 1px; background: var(--rule);
  }
  .contact {
    position: absolute; left: 480px; top: 250px; width: 330px;
    color: var(--ink-light);
  }
  .contact-name {
    font-family: "Great Vibes", cursive;
    font-size: 38px; line-height: 1;
  }
  .contact-tagline {
    font-family: "Open Sans", sans-serif;
    font-size: 13px; color: var(--ink-muted);
    margin-top: 4px; letter-spacing: 0.02em;
  }
  .contact-rule {
    height: 1px; background: var(--rule);
    margin: 16px 0 14px; width: 300px;
  }
  .contact-list { list-style: none; }
  .contact-list li {
    display: flex; align-items: center; gap: 12px;
    font-family: "Open Sans", sans-serif;
    font-size: 15px; line-height: 26px;
  }
  .contact-list svg { flex: none; }
</style>
</head>
<body>
<main class="sheet">
  <section class="card card--front" aria-label="Business card front">
    <h1 class="front-name"><span>Liliana</span><span>Quesada</span></h1>
  </section>

  <section class="card card--back" aria-label="Business card back">
    <svg class="back-ring" width="840" height="480" aria-hidden="true">
      <circle cx="240" cy="400" r="150" fill="none" stroke="var(--ring-grey)" stroke-width="28"/>
    </svg>
    <div class="wordmark">VELIRANDE</div>
    <div class="top-rule"></div>
    <div class="contact">
      <div class="contact-name">Liliana Quesada</div>
      <div class="contact-tagline">unique travel experiences</div>
      <div class="contact-rule"></div>
      <ul class="contact-list">
        <li>
          <svg width="16" height="14" viewBox="0 0 16 14" aria-hidden="true">
            <path d="M1 5 Q8 -1 15 5 L13 7 L11 5 L5 5 L3 7 Z" fill="var(--ink-light)"/>
            <rect x="3" y="7" width="10" height="6" rx="1" fill="var(--ink-light)"/>
            <circle cx="8" cy="10" r="1.6" fill="var(--card-black)"/>
          </svg>
          +55 11 98437.5216
        </li>
        <li>
          <svg width="16" height="16" viewBox="0 0 16 16" aria-hidden="true">
            <circle cx="8" cy="8" r="6.5" fill="none" stroke="var(--ink-light)" stroke-width="1.3"/>
            <ellipse cx="8" cy="8" rx="2.8" ry="6.5" fill="none" stroke="var(--ink-light)" stroke-width="1"/>
            <line x1="1.5" y1="8" x2="14.5" y2="8" stroke="var(--ink-light)" stroke-width="1"/>
          </svg>
          velirande-mail.example
        </li>
        <li>
          <svg width="16" height="12" viewBox="0 0 16 12" aria-hidden="true">
            <rect x="0.6" y="0.6" width="14.8" height="10.8" fill="none" stroke="var(--ink-light)" stroke-width="1.2"/>
            <polyline points="0.6,0.6 8,7 15.4,0.6" fill="none" stroke="var(--ink-light)" stroke-width="1.2"/>
          </svg>
          liliana@velirande-mail.example
        </li>
      </ul>
    </div>
  </section>
</main>
</body>
</html>
```